Flyer für Verkauf von Radondetektoren
Zielgruppe
Ich verkaufe Radondetektoren zur Messung von Radon in Innenräumen. Zielgruppe sind Privatpersonen, Firmen, Genossenschaften und andere Hauseigentümer.
Aufgabenstellung
Ich brauche das Design für meine Messanleitung.
Kreativ - modern - weniger kann mehr sein
Struktur ist wichtigt, es soll also einfach sein zu lesen und zu verstehen, was gemacht werden soll. Können Bulletpoints, Icons mit eingebracht werden.
Wichtig ist auch, dass die beiden Logos 'Luftprüfer.de' und KALVORIX' auf der Messanleitung vorhanden sind. Wobei 'Luftprüfer.de' das Hauptlogo ist.
DIN format dachte ich A4 beidseitig (Text müsste also auf diese Grösse angepasst werden).
Kann natürlich auch Flyer-Format sein oder andere Vorschläge!
Bildmaterial gibt es auf unsere Homepage https://luftprüfer.de und https://luftkollen.se . Diese haben wir bereits gekauft und können verwendet werden. Ich lade sie den bei Bedarf hoch. Es können natürlich auch andere Vorschläge kommen.

```html
<!DOCTYPE html>
<html lang="de">
<head>
<meta charset="utf-8">
<title>Messanleitung – Luftprüfer.de</title>
<link href="https://fonts.googleapis.com/css2?family=Roboto+Condensed:wght@400;700&display=swap" rel="stylesheet">
<style>
  :root{
    --bg:#c0c0c0;
    --page:#ffffff;
    --red:#d41f26;
    --ink:#3c3c3c;
    --muted:#5a5a5a;
    --dark:#222222;
    --sky:#dcebf8;
    --yellow:#f7d716;
    --pinkbg:#fbe3e4;
    --blue:#1c5aa6;
  }
  *{box-sizing:border-box;margin:0;padding:0}
  html,body{width:1200px;height:1200px;overflow:hidden}
  body{background:var(--bg);font-family:"Roboto Condensed",sans-serif;color:var(--ink);position:relative}
  .page{position:absolute;top:230px;width:550px;height:776px;background:var(--page);overflow:hidden}
  .page--front{left:38px;background:linear-gradient(180deg,#fff 0%,#fff 78%,#eeeef0 100%)}
  .page--back{left:612px}
  .abs{position:absolute}

  /* brand marks: name set in text font, one colour, one weight */
  .brand{display:flex;align-items:center;gap:7px}
  .brand__sq{width:16px;height:16px;background:var(--dark);flex:none}
  .brand__name{font-size:19px;line-height:1;font-weight:400;color:var(--dark)}
  .brand__tag{font-size:7.6px;letter-spacing:.6px;color:var(--dark);line-height:1;margin-top:3px;font-weight:400}
  .partner{display:flex;align-items:center;gap:5px;font-size:14px;color:var(--blue);font-weight:400;letter-spacing:.3px}
  .partner__sq{width:9px;height:9px;background:var(--blue)}

  /* front header */
  .hero-sky{left:0;top:0;width:550px;height:230px;background:linear-gradient(180deg,#f6fafe 0%,var(--sky) 100%)}
  .logo-cap{left:0;top:0;width:290px;height:58px;background:#fff;border-radius:0 0 140px 0}
  .hero-art{left:235px;top:6px;width:315px;height:195px;background:linear-gradient(180deg,#e6f0fa 0%,#8f80b8 45%,#5fae4c 80%,#4b9a3f 100%);border-radius:0 0 0 60px}
  .title{left:22px;top:82px;font-size:25px;font-weight:700;color:var(--red);line-height:1}
  .subtitle{left:22px;top:114px;font-size:15px;font-weight:700;color:var(--muted);line-height:18.6px;width:200px}

  .content{left:57px;width:468px;font-size:8.1px;line-height:10.6px;color:var(--muted)}
  .badge{display:inline-block;background:var(--red);color:#fff;font-weight:700;font-size:7.6px;letter-spacing:.4px;border-radius:7px;padding:1px 5px;line-height:10px;vertical-align:middle}
  .step-h{display:flex;align-items:center;gap:7px}
  .step-h h2{font-size:15px;font-weight:700;color:var(--muted);line-height:18px}
  .sub-h{font-size:11px;font-weight:700;color:var(--muted);line-height:14px;margin-bottom:3px}
  ul.dots{list-style:none}
  ul.dots li{position:relative;padding-left:7px}
  ul.dots li::before{content:"";position:absolute;left:0;top:4px;width:3.2px;height:3.2px;border-radius:50%;background:var(--red)}
  b{color:#333}
  .icon{position:absolute;width:26px;height:26px;border-radius:50%;background:var(--pinkbg)}
  .icon svg{position:absolute;left:3px;top:3px;width:20px;height:20px;fill:none;stroke:var(--red);stroke-width:1.3}

  /* back */
  .back-top{left:0;top:0;width:550px;height:210px;background:linear-gradient(135deg,#f4f4f4 0%,#dedede 60%,#d2d2d2 100%)}
  .back-photo{left:0;top:0;width:226px;height:155px;background:linear-gradient(135deg,#6a4b3a 0%,#c49a82 45%,#e8ddd4 100%);border-radius:0 0 120px 0}
  .back-lead{left:275px;top:33px;width:250px}
  .back-lead h2{font-size:16px;font-weight:700;color:var(--muted);margin-top:6px;line-height:20px}
  .back-lead p{font-size:12px;color:var(--muted);line-height:15px;margin-top:4px}
  .final{left:20px;top:323px;width:509px;height:174px;border:1px solid #777;border-radius:10px;text-align:center;font-size:8.1px;line-height:11px;color:var(--muted);padding:0 22px}
  .final .badge{position:absolute;top:-6px;left:50%;transform:translateX(-50%)}
  .final h3{font-size:16px;color:var(--red);font-weight:700;margin-top:14px;line-height:20px}
  .final p{margin-top:4px}
  .ship{margin:12px auto 10px;width:305px;height:40px;background:var(--red);border-radius:7px;color:#fff;font-weight:700;font-size:9px;line-height:12px;display:flex;flex-direction:column;justify-content:center;position:relative}
  .ship__env{position:absolute;left:50%;top:-8px;transform:translateX(-50%);width:16px;height:16px;border-radius:50%;background:#fff}
  .ship__env svg{width:16px;height:16px;stroke:var(--red);fill:none;stroke-width:1.2}
  .notes{left:33px;top:518px;width:500px;font-size:9.2px;line-height:12.3px;color:var(--muted)}
  .notes h3{font-size:11.5px;font-weight:700;color:var(--muted);margin-bottom:6px}
  .notes li{margin-bottom:4.5px;padding-left:10px}
  .notes li::before{top:4.3px}
  .notes a{color:var(--red);text-decoration:none}
  .footer-band{left:0;top:633px;width:550px;height:98px;background:linear-gradient(180deg,#ececec,#f6f6f6);text-align:center}
  .footer-band h4{font-size:12px;color:var(--dark);font-weight:700;margin-top:17px}
  .footer-band p{font-size:9px;color:var(--dark)}
  .copy{left:0;top:740px;width:550px;text-align:center;font-size:7.3px;line-height:9.5px;color:var(--dark)}
</style>
</head>
<body>

<!-- FRONT -->
<section class="page page--front">
  <div class="abs hero-sky"></div>
  <div class="abs hero-art" role="img" aria-label="Illustration: Stadtsilhouette, Häuser und Bäume auf grünen Hügeln unter blauem Himmel"></div>
  <div class="abs logo-cap"></div>
  <div class="abs brand" style="left:26px;top:21px">
    <span class="brand__sq"></span>
    <div><div class="brand__name">Luftprüfer.de</div><div class="brand__tag">SAUBERE RAUMLUFT IM BLICK</div></div>
  </div>
  <div class="abs partner" style="left:456px;top:11px"><span class="partner__sq"></span>KALVORIX</div>
  <svg class="abs" style="left:0;top:170px" width="550" height="70" viewBox="0 0 550 70">
    <path d="M0 65 C150 30 380 18 550 12 L550 70 L0 70Z" fill="#fff"/>
    <path d="M120 30 C300 10 450 15 550 30 L550 38 C440 25 300 20 120 30Z" fill="var(--yellow)"/>
  </svg>
  <h1 class="abs title">Messanleitung</h1>
  <div class="abs subtitle">Für Radonmessungen Von Innenraumluft Mit Passiven Radon Detektoren</div>

  <div class="icon" style="left:19px;top:224px"><svg viewBox="0 0 20 20"><rect x="5" y="9" width="10" height="8" rx="1"/><path d="M7 9V6a3 3 0 0 1 6 0v3"/></svg></div>
  <div class="icon" style="left:19px;top:304px"><svg viewBox="0 0 20 20"><circle cx="11" cy="8" r="5"/><path d="M7.5 11.5 3 17"/></svg></div>
  <div class="icon" style="left:19px;top:380px"><svg viewBox="0 0 20 20"><path d="M3 10 10 4l7 6M5 9v8h10V9M8 17v-4h4v4"/></svg></div>
  <div class="icon" style="left:19px;top:458px"><svg viewBox="0 0 20 20"><rect x="3" y="7" width="14" height="10"/><path d="M6 10h2M12 10h2M6 13h2M12 13h2M3 7l7-4 7 4"/></svg></div>
  <div class="icon" style="left:19px;top:563px"><svg viewBox="0 0 20 20"><path d="M3 8 10 4l7 4H3zM5 9v6M8 9v6M12 9v6M15 9v6M3 16h14"/></svg></div>

  <div class="abs content" style="top:204px">
    <div class="step-h"><span class="badge">SCHRITT 1</span><h2>Registrierung Und Anmeldung</h2></div>
    <p>Wenn Sie Neukunde sind, legen Sie bitte zunächst ein neues Benutzerkonto auf unserem Online-Porta https://portal.kalvorix-labor.se/de an. Anschließend können Sie die Radondetektoren registrieren. Vermerken Sie den Start der Messung (Datum und Uhrzeit), die Messorte (Raum und Etage) sowie die 9-stellige Seriennummer der Detektoren, die Sie auf der Verpackung oder auf der Unterseite der jeweiligen Detektoren finden.<br>Firmenkunden haben die Möglichkeit eine Excel-Datei als Hilfsmittel herunterzuladen, die Sie ausfüllen und dann wieder hochladen.</p>
  </div>

  <div class="abs content" style="top:287px">
    <div class="step-h"><span class="badge">SCHRITT 2</span><h2>Platzierung Der Detektoren</h2></div>
    <p style="margin-top:4px">Bevor Sie die Detektoren der Verpackung entnehmen, überlegen Sie wo genau Sie die Radondetektoren platzieren wollen. Die Radon-messung beginnt, sobald Sie die radondichten Verpackungen öffnen. Beachten Sie bei der Platzierung zunächst die <b>Auswahl der Räume</b> und <b>die Positionierung der Radondetektoren im Raum.</b></p>
    <p style="margin-top:5px">Für eine zuverlässige Radonmessung empfehlen wir wie folgt vorzugehen:</p>
  </div>

  <div class="abs content" style="top:367px">
    <span class="badge">DIE AUSWAHL DER RÄUME:</span>
    <div class="sub-h" style="margin-top:4px">Radonmessungen für Einfamilienhäuser:</div>
    <ul class="dots">
      <li>Es sollten mindestens zwei Wohnräume und pro bewohnte Etage mindestens ein Wohnraum gemessen werden. Wählen Sie Räume aus, in denen Sie sich oft aufhalten (z.B. das Wohn- und Schlafzimmer). Vermeiden Sie aber Räume, in denen das Fenster mehrere Stunden am Tag oder in der Nacht geöffnet ist.</li>
      <li>Insofern Sie einen Keller haben, empfehlen wir alle Kellerräume zu messen, da hier meist das größte Risiko einer erhöhten Radonkonzentration erwartet wird.</li>
    </ul>
  </div>

  <div class="abs content" style="top:462px">
    <div class="sub-h">Radonmessungen für Mehrfamilienhäuser, Wohnungen und Wohnkomplexen:</div>
    <ul class="dots">
      <li>Alle Wohnungen mit direktem Bodenkontakt sowie mindestens eine Wohnung pro Etage sollten gemessen werden. Wählen Sie dabei Wohnungen, die an Aufzügen oder Luftschächten liegen.</li>
      <li>In größeren Wohnkomplexen sollten insgesamt mindestens 20% aller Wohnungen in einem Gebäude gemessen werden.</li>
      <li>Es sollten mindestens zwei Wohnräume pro ausgewählte Wohnung gemessen werden. Wählen Sie Räume aus, in denen Sie sich oft aufhalten (z.B. das Wohn- und Schlafzimmer). Vermeiden Sie aber Räume, in denen das Fenster mehrere Stunden am Tag oder in der Nacht geöffnet ist.</li>
      <li>Selbst bei einer Einzimmerwohnung sollten Sie zwei Detektoren aufstellen.</li>
    </ul>
  </div>

  <div class="abs content" style="top:567px">
    <div class="sub-h">Radonmessungen für Arbeitsplätze und öffentliche Gebäude:</div>
    <ul class="dots">
      <li>Wählen Sie Räume, die regelmäßig mehr als vier Stunden pro Tag genutzt werden.</li>
      <li>Messen Sie alle unterirdischen Räumlichkeiten, da hier meist das größte Risiko einer erhöhten Radonkonzentration erwartet wird.</li>
      <li>Messen Sie alle Räume im Erdgeschoß. Für größere Räumlichkeiten empfehlen wir einen Detektor pro 200 m².</li>
      <li>In den oberen Etagen sollten Sie mit mindestens zwei Detektoren, sowie mindestens einem Detektor pro 200 m² messen.</li>
      <li>Falls Ihr Arbeitsplatz in einem Radon-Vorsorgegebiet liegt und somit der Messpflicht unterliegt, muss die Messdauer von 12 Monaten eingehalten werden.</li>
    </ul>
  </div>

  <div class="abs content" style="top:654px">
    <span class="badge">PLATZIERUNG DER DETEKTOREN IM RAUM:</span>
    <ul class="dots" style="margin-top:5px">
      <li>Platzieren Sie die Detektoren in einem Mindestabstand von 20 cm zu Wänden, 50 cm zu Abluftsventilen, sowie 1,50 m zu Fenstern, Außentüren, Zuluftsventilen und Heizkörpern.</li>
      <li>Stellen Sie die Detektoren nicht auf dem Boden, an starken Wärmequellen oder Luftströmen auf. Vermeiden Sie auch Räume mit hoher Luftfeuchtigkeit, wie zum Beispiel das Badezimmer.</li>
      <li>Die Detektoren können entweder stehend (auf einem Tisch, im Regal oder einer Schrankwand) oder hängend mitten im Raum (z.B. von einer Lampe) platziert werden.</li>
      <li>Stellen Sie die Detektoren während der gesamten Messdauer nicht um.</li>
      <li>Versuchen Sie nicht das Gehäuse der Detektoren zu öffnen und platzieren Sie diese immer außer Reichweite von Kindern.</li>
    </ul>
  </div>
</section>

<!-- BACK -->
<section class="page page--back">
  <div class="abs back-top"></div>
  <div class="abs back-photo" role="img" aria-label="Foto: Mutter mit zwei Kleinkindern, die auf ein Tablet schauen"></div>
  <svg class="abs" style="left:0;top:130px" width="550" height="90" viewBox="0 0 550 90">
    <path d="M0 25 C160 -5 420 10 550 60 L550 90 L0 90Z" fill="#fff"/>
  </svg>
  <div class="abs back-lead">
    <span class="badge">SCHRITT 3</span>
    <h2>Radonmessung</h2>
    <p>Die Radonmessung beginnt, sobald Sie die radondichten Verpackungen öffnen.</p>
  </div>

  <div class="icon" style="left:18px;top:175px"><svg viewBox="0 0 20 20"><circle cx="10" cy="11" r="6"/><path d="M10 5v6l4 2"/></svg></div>
  <div class="icon" style="left:18px;top:242px"><svg viewBox="0 0 20 20"><rect x="3" y="4" width="14" height="10"/><path d="M5 12l3-3 3 2 4-4M10 14v3M7 17h6"/></svg></div>

  <div class="abs content" style="left:58px;top:160px;width:470px">
    <p>Bitte halten Sie die Messdauer wie folgt ein:</p>
    <div class="sub-h" style="margin-top:3px">Kurzzeitmessung:</div>
    <ul class="dots">
      <li>Mindestmessdauer 10 Tage (bis hin zu 30 Tagen).</li>
      <li>Führen Sie die Messung vorzugsweise in der Heizperiode (1. Oktober – 30. April) durch.</li>
      <li>Kurzzeitmessungen werden oft beim Kauf oder Verkauf von Immobilien genutzt, um ein mögliches Gefährdungspotential abschätzen zu können, oder wenn die Zeit nicht ausreicht, um eine Langzeitmessung durchzuführen.</li>
    </ul>
  </div>
  <div class="abs content" style="left:58px;top:245px;width:470px">
    <div class="sub-h">Langzeitmessung:</div>
    <ul class="dots">
      <li>Mindestmessdauer 3 Monate während der Heizperiode (1. Oktober – 30. April).</li>
      <li>Um einen Jahresmittelwert der Radonkonzentration in Innenräumen ermitteln zu können, halten Sie die Messdauer von 12 Monaten ein.</li>
      <li><b>Falls Ihr Arbeitsplatz in einem Radon-Vorsorgegebiet liegt und somit der Messpflicht unterliegt, muss die Messdauer von 12 Monaten eingehalten werden.</b></li>
    </ul>
  </div>

  <div class="abs final">
    <span class="badge">SCHRITT 4</span>
    <h3>Abschluss Der Radonmessung Mit Abschliessendem Prüfbericht</h3>
    <p>Nach Ablauf der Messdauer, loggen Sie sich auf <b>https://portal.kalvorix-labor.se/de</b> in Ihrem Account ein. Vermerken Sie hier das Ende der Messung und senden Sie anschließend alle Radondetektoren ausreichend frankiert in einem Umschlag oder einem Karton <b>zeitnah</b> an unsere Rücksendeadresse:</p>
    <div class="ship">
      <span class="ship__env"><svg viewBox="0 0 16 16"><rect x="3.5" y="5" width="9" height="6"/><path d="M3.5 5 8 8.5 12.5 5"/></svg></span>
      <span>www.Luftprüfer.de</span>
      <span>Lindenallee 14 – 27612 Nordholm – Deutschland</span>
    </div>
    <p>Sobald die Radondetektoren im Labor von KALVORIX eingetroffen sind, werden diese fachgerecht analysiert und die Ergebnisse der Radonmessung ausgewertet. Ein vollständiger Prüfbericht wird Ihnen innerhalb 36 Stunden nach Erhalt der Detektoren im Labor per E-Mail zugeschickt.</p>
  </div>

  <div class="abs notes">
    <h3>Weitere Hinweise:</h3>
    <ul class="dots">
      <li>Bitte beachten Sie, dass die Radonmessung innerhalb von 15 Monaten nach Kaufdatum abgeschlossen sein muss.</li>
      <li>Versuchen Sie nicht das Gehäuse der Detektoren zu öffnen und platzieren Sie diese immer außer Reichweite von Kindern.</li>
      <li>Während der gesamten Messdauer dürfen die Detektoren nicht an einem anderen Ort umplatziert werden.</li>
      <li>Durch die Anmeldung auf der Website <a>https://portal.kalvorix-labor.se/de</a> und die Eingabe der erforderlichen Daten bestätigt der/die Wohnungseigentümer*in/Messverantwortliche, dass er/sie die Messanleitung befolgt hat und die Detektoren gemäß den Anweisungen korrekt platziert wurden.</li>
    </ul>
  </div>

  <div class="abs footer-band">
    <h4>Datenschutz (Gdpr), Impressum Und Agbs:</h4>
    <p>Mehr Information Dazu Finden Sie Unter</p>
    <div class="brand" style="justify-content:center;margin-top:9px">
      <span class="brand__sq" style="width:18px;height:18px"></span>
      <div style="text-align:left"><div class="brand__name" style="font-size:22px">Luftprüfer.de</div><div class="brand__tag" style="font-size:9px">SAUBERE RAUMLUFT IM BLICK</div></div>
    </div>
  </div>
  <div class="abs copy">copyright © 2023 Nordluft Mätteknik Ab - Alle Rechte Vorbehalten<br>https://www.luftprüfer.de</div>
  <div class="abs partner" style="left:450px;top:744px"><span class="partner__sq"></span>KALVORIX</div>
</section>

</body>
</html>
```